Tallow Crest Business Card

We need a business card designed for a a company called "Tallow Crest". We offer consulting, coaching and training to business leaders and coaches (across the world) using the latest findings in neuroscience, social and emotional intelligence and positive psychology. The final design should communicate the use of brain science to create sustainable relationships.

The card should be doublesided. The logo is attached and names and titles will be provided to the successful designer. Thank you.

Industry/Entity Type

Training

```html
<!DOCTYPE html>
<html lang="en">
<head>
<meta charset="utf-8">
<title>Tallow Crest Business Card</title>
<link rel="stylesheet" href="https://fonts.googleapis.com/css2?family=Open+Sans:wght@400;600;700&display=swap">
<style>
  :root {
    --brand-blue: #0a8bbd;
    --brand-lime: #b7d30b;
    --ink: #3a3a3a;
    --card: #ffffff;
    --stage: #e9e9e9;
  }
  * { margin: 0; padding: 0; box-sizing: border-box; }
  html, body { width: 1200px; height: 900px; overflow: hidden; }
  body {
    background: var(--stage);
    font-family: "Open Sans", sans-serif;
    position: relative;
  }
  .card {
    position: absolute;
    top: 308px;
    width: 516px;
    height: 284px;
    background: var(--card);
    box-shadow: 0 1px 4px rgba(0,0,0,0.15);
  }
  .card--front { left: 72px; }
  .card--back { left: 615px; }

  .brand {
    display: flex;
    align-items: center;
    gap: 10px;
    color: var(--brand-blue);
    font-weight: 700;
    white-space: nowrap;
  }
  .brand__dot {
    width: 16px; height: 16px;
    border-radius: 50%;
    background: var(--brand-lime);
    flex: none;
  }
  .card--front .brand {
    position: absolute;
    left: 50%; top: 50%;
    transform: translate(-50%, -50%);
    font-size: 40px;
  }
  .card--back .brand {
    position: absolute;
    left: 36px; top: 50%;
    transform: translateY(-50%);
    font-size: 24px;
    gap: 7px;
  }
  .card--back .brand__dot { width: 11px; height: 11px; }

  .divider {
    position: absolute;
    left: 256px; top: 64px;
    width: 2px; height: 162px;
    background: var(--brand-blue);
  }
  .contact {
    position: absolute;
    left: 286px; top: 68px;
    color: var(--ink);
  }
  .contact__name {
    font-size: 16.5px;
    font-weight: 600;
    color: var(--brand-blue);
    line-height: 1.2;
  }
  .contact__title {
    font-size: 11.5px;
    font-weight: 700;
    line-height: 1.4;
    margin-bottom: 10px;
  }
  .contact__list { list-style: none; }
  .contact__item {
    display: flex;
    align-items: flex-start;
    gap: 8px;
    font-size: 11.5px;
    line-height: 15.5px;
  }
  .contact__item--gap { margin-top: 7px; }
  .contact__icon {
    width: 10px; height: 11px;
    margin-top: 2px;
    flex: none;
    fill: var(--brand-blue);
  }
</style>
</head>
<body>
  <section class="card card--front" aria-label="Card front">
    <div class="brand"><span class="brand__dot"></span>Tallow Crest</div>
  </section>

  <section class="card card--back" aria-label="Card back">
    <div class="brand"><span class="brand__dot"></span>Tallow Crest</div>
    <div class="divider"></div>
    <div class="contact">
      <p class="contact__name">Renata Holloway</p>
      <p class="contact__title">managing director</p>
      <ul class="contact__list">
        <li class="contact__item">
          <svg class="contact__icon" viewBox="0 0 10 12"><path d="M5 0a4 4 0 0 0-4 4c0 3 4 8 4 8s4-5 4-8a4 4 0 0 0-4-4zm0 5.6a1.6 1.6 0 1 1 0-3.2 1.6 1.6 0 0 1 0 3.2z"/></svg>
          <span>48 Alder Lane<br>Brookfield, Ohio 44403</span>
        </li>
        <li class="contact__item">
          <svg class="contact__icon" viewBox="0 0 10 12"><path d="M2 0h6a1 1 0 0 1 1 1v10a1 1 0 0 1-1 1H2a1 1 0 0 1-1-1V1a1 1 0 0 1 1-1zm.4 1.2v8h5.2v-8zM5 9.8a.6.6 0 1 0 0 1.2.6.6 0 0 0 0-1.2z"/></svg>
          <span>410 262 73 19</span>
        </li>
        <li class="contact__item">
          <svg class="contact__icon" viewBox="0 0 12 12"><circle cx="6" cy="6" r="6"/><path d="M3.6 3.2l1.2-.4.8 1.6-.7.6c.3.8.9 1.5 1.7 1.9l.6-.7 1.6.8-.4 1.2c-2.4 0-4.6-2.2-4.8-5z" fill="#fff"/></svg>
          <span>410 262 73 20</span>
        </li>
        <li class="contact__item contact__item--gap">
          <svg class="contact__icon" viewBox="0 0 12 12"><path d="M0 2.5h12v7H0zM.8 3.2 6 6.8l5.2-3.6v-.1H.8z"/><path d="M.8 3.2 6 6.8l5.2-3.6" fill="none" stroke="#fff" stroke-width=".8"/></svg>
          <span>info@tallowcrest.com</span>
        </li>
        <li class="contact__item">
          <svg class="contact__icon" viewBox="0 0 12 12"><circle cx="6" cy="6" r="5.4" fill="none" stroke="#0a8bbd" stroke-width="1.1"/><ellipse cx="6" cy="6" rx="2.3" ry="5.4" fill="none" stroke="#0a8bbd" stroke-width="1"/><path d="M.6 6h10.8M1.5 3.3h9M1.5 8.7h9" stroke="#0a8bbd" stroke-width=".9"/></svg>
          <span>www.tallowcrest.com</span>
        </li>
      </ul>
    </div>
  </section>
</body>
</html>
```